Business Cards

We were billed for this because the project timed out. Please give me another designed to open this back up. I was not happy with the last designs (that I was charged for).
we are also using the logo with Revitalizing Pools One Drop at a Time
Also want to utilize Where Healthy Water is our Commitment.

Contact Information for Business Card

Marlowe Stone Group Inc

```html
<!DOCTYPE html>
<html lang="en">
<head>
<meta charset="utf-8">
<title>Marlowe Stone Group Inc — Business Cards</title>
<link href="https://fonts.googleapis.com/css2?family=Montserrat:wght@400;500;700;800&display=swap" rel="stylesheet">
<style>
  :root {
    --stage: #1e1e1e;
    --brand-blue: #1463b0;
    --brand-deep: #0f56a3;
    --brand-sky: #4aa3dc;
    --ink: #3a3a3a;
    --ink-soft: #555555;
    --paper: #ffffff;
  }
  * { margin: 0; padding: 0; box-sizing: border-box; }
  html, body {
    width: 1200px; height: 988px; overflow: hidden;
    background: var(--stage);
    font-family: "Montserrat", Arial, sans-serif;
  }
  .card {
    position: absolute;
    width: 700px; height: 400px;
    border-radius: 22px;
    overflow: hidden;
    box-shadow: 0 14px 30px rgba(0,0,0,.55);
  }

  /* Back side */
  .card--back {
    left: 110px; top: 54px;
    background: var(--brand-blue);
  }
  .back-pattern {
    position: absolute; inset: 0;
    background: linear-gradient(135deg, #1a6dbd 0%, #1463b0 50%, #0f56a3 100%);
  }
  .back-content {
    position: absolute; inset: 0;
    display: flex; flex-direction: column;
    align-items: center; justify-content: center;
    color: var(--paper);
    text-align: center;
  }
  .back-name {
    font-weight: 800; font-size: 30px; letter-spacing: 1px;
    text-transform: uppercase;
  }
  .back-motto {
    margin-top: 30px;
    font-weight: 500; font-size: 22px; letter-spacing: 4px;
  }

  /* Front side */
  .card--front {
    left: 390px; top: 534px;
    background: var(--paper);
  }
  .front-band { position: absolute; left: 0; top: 0; width: 700px; height: 400px; }
  .brand-block {
    position: absolute; left: 46px; top: 142px; width: 300px;
    text-align: center;
  }
  .brand-name {
    font-weight: 800; font-size: 24px; color: var(--brand-blue);
    letter-spacing: .5px; text-transform: uppercase;
  }
  .brand-tagline {
    margin-top: 6px;
    font-weight: 500; font-size: 10.5px; color: var(--ink-soft);
    letter-spacing: 1.6px; text-transform: uppercase;
  }
  .divider {
    position: absolute; left: 372px; top: 78px;
    width: 1.5px; height: 170px; background: var(--brand-blue);
  }
  .contact {
    position: absolute; left: 396px; top: 74px;
    color: var(--ink); font-size: 15px; line-height: 1.32;
  }
  .contact-name {
    font-weight: 700; font-size: 25px; letter-spacing: .5px; line-height: 1.1;
  }
  .contact-name .first { color: var(--brand-deep); }
  .contact-name .last { color: var(--brand-sky); }
  .contact-role { font-size: 15px; margin-bottom: 12px; }
  .contact-address { margin-bottom: 12px; }
  .contact-line { display: flex; align-items: center; gap: 7px; }
  .contact-line svg { width: 13px; height: 13px; flex: none; }
  .website {
    position: absolute; right: 34px; bottom: 26px;
    display: flex; align-items: center; gap: 8px;
    color: var(--paper); font-size: 15px; letter-spacing: .4px;
  }
  .website .domain { color: #8fc8ee; }
  .website svg { width: 14px; height: 14px; }
</style>
</head>
<body>

<section class="card card--back" aria-label="Business card back">
  <div class="back-pattern" role="img" aria-label="Repeating brand monogram pattern in tonal blues"></div>
  <div class="back-content">
    <div class="back-name">Marlowe Stone Group</div>
    <div class="back-motto">Healthy Water is our Commitment</div>
  </div>
</section>

<section class="card card--front" aria-label="Business card front">
  <svg class="front-band" viewBox="0 0 700 400" aria-hidden="true">
    <path d="M0 330 L470 330 C485 330 488 318 492 310 C497 300 505 296 520 296 L700 296 L700 400 L0 400 Z" fill="#4aa3dc"/>
    <path d="M0 344 L470 344 C492 344 496 330 500 322 C505 313 512 310 526 310 L700 310 L700 400 L0 400 Z" fill="#ffffff"/>
    <path d="M0 350 L472 350 C494 350 499 336 503 328 C508 319 515 316 528 316 L700 316 L700 400 L0 400 Z" fill="#1463b0"/>
  </svg>

  <div class="brand-block">
    <div class="brand-name">Marlowe Stone Group</div>
    <div class="brand-tagline">Revitalizing Pools One Drop at a Time</div>
  </div>

  <div class="divider"></div>

  <div class="contact">
    <div class="contact-name"><span class="first">DANA</span> <span class="last">WHITFIELD</span></div>
    <div class="contact-role">CEO/Founder</div>
    <div class="contact-address">48 Harbor Lane, Suite 210<br>Lakeview, AB 42615</div>
    <div class="contact-line">
      <svg viewBox="0 0 16 16"><path d="M3 1.5 L6 1.5 L7 5 L5.2 6.3 C6 8.2 7.8 10 9.7 10.8 L11 9 L14.5 10 L14.5 13 C14.5 14 13.6 14.6 12.6 14.5 C6.8 13.9 2.1 9.2 1.5 3.4 C1.4 2.4 2 1.5 3 1.5 Z" fill="#4aa3dc"/></svg>
      <span>555-204-7718</span>
    </div>
    <div class="contact-line">
      <svg viewBox="0 0 16 16"><rect x="1" y="3.5" width="14" height="9.5" rx="1.2" fill="#4aa3dc"/><path d="M1.5 4.2 L8 9 L14.5 4.2" fill="none" stroke="#ffffff" stroke-width="1.3"/></svg>
      <span>info@marlowestonegroup.com</span>
    </div>
  </div>

  <div class="website">
    <svg viewBox="0 0 16 16"><circle cx="8" cy="8" r="7" fill="none" stroke="#ffffff" stroke-width="1.4"/><ellipse cx="8" cy="8" rx="3" ry="7" fill="none" stroke="#ffffff" stroke-width="1.2"/><line x1="1" y1="8" x2="15" y2="8" stroke="#ffffff" stroke-width="1.2"/></svg>
    <span>www.<span class="domain">marlowestonegroup</span>.com</span>
  </div>
</section>

</body>
</html>
```